KRTO Membership Web Design Project

We need a website design for KRTO membership. We need something different from what we currently have. See what we currently have: http://www.wovarclub.example/ptx4/

Make provision for where members bushiness can be advertised.
Updates

We need a box for advertising members projects/business.

Make provision for where members bushiness / products can be advertised.

Target Market(s)

For members of KRTO and Intending members. Membership is for married men only.

Requirements
Must have
• Make provision for where members bushiness can be advertised.

You are to redesign: http://www.wovarclub.example/ptx4/

```html
<!DOCTYPE html>
<html lang="en">
<head>
<meta charset="utf-8">
<title>KRTO Members Portal</title>
<link rel="stylesheet" href="https://fonts.googleapis.com/css2?family=Source+Sans+3:wght@400;600&family=Arimo:wght@400&display=swap">
<style>
:root{
  --blue:#2a62ad;
  --blue-dark:#1f4f93;
  --blue-light:#3b77c4;
  --title:#0f5a99;
  --text:#555;
  --link:#2a5c9a;
  --green:#7dbf2a;
  --line:#d6d9de;
  --hero-bg:#eef0f3;
  --footer-bg:#f3f4f6;
}
*{box-sizing:border-box;margin:0;padding:0}
html,body{width:785px;height:1200px;overflow:hidden;background:#fff}
body{position:relative;font-family:"Source Sans 3",Arial,sans-serif;color:var(--text);font-size:9.5px}
.abs{position:absolute}
/* header */
.brand{left:23px;top:20px;display:flex;align-items:center;gap:8px}
.brand-mark{width:52px;height:52px;border-radius:50%;background:var(--blue)}
.brand-name{font-size:17px;font-weight:600;color:var(--blue-dark);line-height:1.05}
.field{top:19px;height:17px;border:1px solid #c9ccd1;background:#fff;font-size:9px;color:#888;padding:2px 6px}
.login-btn{left:693px;top:17px;width:58px;height:19px;border-radius:3px;background:linear-gradient(#9ad34a,var(--green));color:#fff;font-weight:600;font-size:11px;text-align:center;line-height:19px}
.forgot{left:678px;top:44px;font-size:9px;color:var(--link)}
.search{left:592px;top:63px;width:162px;height:22px;border:1px solid #c9ccd1;font-size:9px;font-style:italic;color:#666;padding:5px 7px}
.search svg{position:absolute;right:7px;top:5px}
/* nav */
.nav{left:0;top:95px;width:785px;height:33px;background:linear-gradient(var(--blue-light),var(--blue));display:flex}
.nav a{color:#fff;text-decoration:none;font-size:10.5px;text-align:center;line-height:33px;border-right:1px solid #5b8cc9}
/* hero */
.hero{left:0;top:128px;width:785px;height:282px;background:var(--hero-bg);overflow:hidden}
.hero-title{left:40px;top:172px;font-size:24px;font-weight:600;color:var(--title)}
.hero-sub{left:40px;top:200px;font-size:18px;color:#222}
.hero-copy{left:39px;top:231px;width:275px;font-size:8.6px;line-height:14px;color:#444}
.hero-copy p{margin-bottom:8px}
.btn{background:linear-gradient(var(--blue-light),var(--blue-dark));color:#fff;border-radius:3px;font-size:9.5px;text-align:center}
.hero-btn{left:41px;top:323px;width:74px;height:22px;line-height:22px}
.hero-photo{left:349px;top:145px;width:384px;height:240px;border:4px solid #fff;box-shadow:0 0 4px rgba(0,0,0,.35);background:linear-gradient(135deg,#c9ced4,#e8eaec 40%,#a7a9ab 70%,#d9dbde)}
.arrow{top:254px;width:22px;height:22px;background:var(--blue-dark);color:#fff;text-align:center;line-height:22px;font-size:12px}
/* cards */
.card{top:417px;width:241px;height:114px;border-radius:4px;overflow:hidden;box-shadow:0 1px 3px rgba(0,0,0,.35)}
.card-head{height:35px;background:var(--blue-dark);color:#fff;font-family:Arimo,Arial,sans-serif;font-size:11.5px;line-height:35px;padding:0 32px 0 11px;white-space:nowrap;position:relative}
.card-head svg{position:absolute;right:8px;top:9px}
.card-img{height:79px}
/* welcome */
.welcome-title{left:29px;top:549px;font-size:15px;color:var(--title)}
.welcome-copy{left:29px;top:578px;width:475px;font-size:8.4px;line-height:15px;color:var(--link)}
.welcome-copy p{margin-bottom:9px}
.read-btn{left:418px;top:683px;width:84px;height:21px;line-height:21px}
/* news */
.news{left:20px;top:712px;width:494px;height:215px;border:1px solid var(--line);background:#fafafa}
.news-title{left:12px;top:6px;font-size:15px;color:var(--blue-dark)}
.news-nav{right:12px;top:11px;display:flex;gap:3px}
.news-item{left:12px;width:468px;display:flex;gap:13px}
.cal{width:50px;height:46px;flex:none;border-radius:4px;background:#e9ebee;overflow:hidden;text-align:center;color:var(--blue-dark)}
.cal-top{height:13px;background:var(--blue-light)}
.cal-day{font-size:15px;line-height:15px;font-weight:600}
.cal-mon{font-size:8px}
.news-text{font-size:8.4px;line-height:13px;color:#555}
.news-more{display:block;text-align:right;margin-top:7px;color:var(--link);font-size:8.5px;padding-right:18px}
.divider{left:14px;top:107px;width:466px;height:1px;background:var(--line)}
/* business */
.business{left:29px;top:935px;width:482px;height:153px;background:#f1f2f4}
.business-img{width:249px;height:153px;background:linear-gradient(120deg,#dbe8f5,#9cc0e6 55%,#eaf2fb)}
.business-title{left:265px;top:24px;font-family:Arimo,Arial,sans-serif;font-size:18px;color:var(--blue-dark)}
.business-copy{left:265px;top:56px;width:210px;font-family:Arimo,Arial,sans-serif;font-size:10.5px;line-height:17px;color:#333}
/* sidebar */
.comments{left:535px;top:546px;width:232px;height:297px;border:1px solid var(--line);background:#fff}
.comments-head{height:36px;background:linear-gradient(var(--blue-light),var(--blue));color:#fff;font-size:14.5px;line-height:36px;padding-left:15px}
.comment{padding:10px 13px 7px;border-bottom:1px solid var(--line);height:78px}
.comment:last-child{border-bottom:none}
.comment-date{font-size:10.5px;font-weight:600;color:var(--title)}
.comment-text{font-size:8.4px;line-height:12px;margin-top:3px}
.comment-more{font-size:8.5px;color:var(--link);margin-top:3px}
.saving{left:535px;top:843px;width:232px;height:277px;background:#fff;box-shadow:-3px 0 6px rgba(0,0,0,.08)}
.saving-img{left:100px;top:18px;width:125px;height:168px;background:linear-gradient(160deg,#e6c4a6,#d0d4d8 45%,#b7bcc2);border-radius:40% 40% 30% 30%}
.saving-learn{left:40px;top:197px;font-family:Arimo,Arial,sans-serif;font-size:16px;color:var(--green)}
.saving-copy{left:40px;top:218px;font-family:Arimo,Arial,sans-serif;font-size:11px;line-height:17px;color:var(--blue-dark)}
/* footer */
.footer{left:0;top:1120px;width:785px;height:80px;background:var(--footer-bg)}
.footer-nav{left:23px;top:19px;font-size:9px;color:#444;word-spacing:1px}
.footer-nav span{margin:0 9px}
.footer-copy{left:24px;top:42px;font-size:8.6px;color:#444}
.social{right:40px;top:14px;display:flex;gap:12px}
.social i{width:18px;height:18px;border-radius:50%;background:#6b6f75;display:block}
</style>
</head>
<body>

<header>
  <div class="abs brand"><span class="brand-mark"></span><span class="brand-name">Kindred Road<br>members portal</span></div>
  <div class="abs field" style="left:455px;width:113px">Username</div>
  <div class="abs field" style="left:574px;width:113px">Password</div>
  <div class="abs login-btn">Login</div>
  <div class="abs forgot">Forgot Password ?</div>
  <div class="abs search">Search here..
    <svg width="10" height="10" viewBox="0 0 10 10"><circle cx="4" cy="4" r="3" fill="none" stroke="#2a62ad" stroke-width="1.6"/><path d="M6.3 6.3 9 9" stroke="#2a62ad" stroke-width="1.8"/></svg>
  </div>
</header>

<nav class="abs nav">
  <a style="width:92px">Home</a>
  <a style="width:93px">About Us</a>
  <a style="width:107px">Membership</a>
  <a style="width:124px">Member Projects</a>
  <a style="width:140px">Membership Levels</a>
  <a style="width:71px">Links</a>
  <a style="width:97px;border-right:none">Contact Us</a>
</nav>

<section class="abs hero">
  <svg class="abs" style="left:0;top:0" width="785" height="282"><path d="M0 150 C120 30 260 10 380 40 L380 282 L0 282Z" fill="#f7f8f9"/></svg>
</section>
<h1 class="abs hero-title">Kindred Road</h1>
<div class="abs hero-sub">tittle line of Jesus Family</div>
<div class="abs hero-copy">
  <p>Brightmoor Web Studio is a web service company, offering a wide range of services which range from designing and dev3elopment, that is covering almost all the fields in the best possible way.</p>
  <p>To be the best we know what and how to present beautifully the working of the client's need and their advantages be highlighted.</p>
</div>
<div class="abs btn hero-btn">Learn More &rsaquo;</div>
<div class="abs hero-photo" role="img" aria-label="Photo of smiling businessmen in suits"></div>
<div class="abs arrow" style="left:349px">&lsaquo;</div>
<div class="abs arrow" style="left:711px">&rsaquo;</div>

<svg width="0" height="0" style="position:absolute"><defs><symbol id="go" viewBox="0 0 18 18"><circle cx="9" cy="9" r="8.5" fill="#fff"/><path d="M5 9h6M8.5 5.5 12 9l-3.5 3.5" stroke="#1f4f93" stroke-width="2.2" fill="none"/></symbol></defs></svg>

<div class="abs card" style="left:17px">
  <div class="card-head">OUR OBJECTIVES<svg width="17" height="17"><use href="#go"/></svg></div>
  <div class="card-img" role="img" aria-label="Man climbing a ladder over a world map" style="background:linear-gradient(120deg,#2d5ea3,#8fb6e0 55%,#dfe9f5)"></div>
</div>
<div class="abs card" style="left:271px">
  <div class="card-head">MEMBERSHIP LEVELS/BENEFITS<svg width="17" height="17"><use href="#go"/></svg></div>
  <div class="card-img" role="img" aria-label="Close-up of the word membership printed on paper" style="background:linear-gradient(90deg,#3a3a3a,#e9e7e2 30%,#f3f1ec)"></div>
</div>
<div class="abs card" style="left:527px">
  <div class="card-head">REGISTRATION<svg width="17" height="17"><use href="#go"/></svg></div>
  <div class="card-img" role="img" aria-label="Fountain pen resting on a notebook" style="background:linear-gradient(160deg,#f4f4f4,#d9d9d9 55%,#b9a47a)"></div>
</div>

<h2 class="abs welcome-title" style="font-weight:400">Welcome to Our Website Mainpage</h2>
<div class="abs welcome-copy">
  <p>Kindred Road Trust Order (KRTO) was established on the 19th day of July 2008 by a group of Christian men from various Church denominations. KRTO is an interdenominational and non-denominational fellowship, born out of a great and overwhelming burden for our generation and a strong desire to see the kingdom of God come and His will be done on Earth as it is in Heaven.</p>
  <p>Thus,Wanna get ahead in the competition with other websites…. Brightmoor Web Studio provide you with an attractive and most convincing website to enhance your marketing goals.</p>
</div>
<div class="abs btn read-btn">READ MORE &rsaquo;</div>

<section class="abs news">
  <h3 class="abs news-title" style="font-weight:400">Latest News</h3>
  <div class="abs news-nav">
    <svg width="13" height="13" viewBox="0 0 18 18"><circle cx="9" cy="9" r="8.5" fill="#8a8f96"/><path d="M13 9H7M9.5 5.5 6 9l3.5 3.5" stroke="#fff" stroke-width="2.2" fill="none"/></svg>
    <svg width="13" height="13" viewBox="0 0 18 18"><circle cx="9" cy="9" r="8.5" fill="#8a8f96"/><path d="M5 9h6M8.5 5.5 12 9l-3.5 3.5" stroke="#fff" stroke-width="2.2" fill="none"/></svg>
  </div>
  <div class="abs news-item" style="top:36px">
    <div class="cal"><div class="cal-top"></div><div class="cal-day">22</div><div class="cal-mon">JUNE</div></div>
    <div class="news-text">Brightmoor Web Studio provides you the Search Engine Optimization making your website search engine friendly.Brightmoor Web Studio provides you the Search Engine Optimization making your website search engine friendly.<span class="news-more">READ MORE</span></div>
  </div>
  <div class="abs divider"></div>
  <div class="abs news-item" style="top:126px">
    <div class="cal"><div class="cal-top"></div><div class="cal-day">22</div><div class="cal-mon">JUNE</div></div>
    <div class="news-text">Brightmoor Web Studio provides you the Search Engine Optimization making your website search engine friendly.Brightmoor Web Studio provides you the Search Engine Optimization making your website search engine friendly.<span class="news-more">READ MORE</span></div>
  </div>
</section>

<section class="abs business">
  <div class="business-img" role="img" aria-label="Blue-toned desk globe beside a phone"></div>
  <h3 class="abs business-title" style="font-weight:400">MEMBERS BUSINESS</h3>
  <p class="abs business-copy">Lorem Ipsum is simply dummy text of the printing and typesetting industry.</p>
  <svg class="abs" style="left:443px;top:118px" width="22" height="22" viewBox="0 0 18 18"><circle cx="9" cy="9" r="8.5" fill="#0f3f73"/><path d="M5 9h6M8.5 5.5 12 9l-3.5 3.5" stroke="#fff" stroke-width="2" fill="none"/></svg>
</section>

<aside class="abs comments">
  <div class="comments-head">Recent Comments &amp; Blog</div>
  <div class="comment"><div class="comment-date">20.March.2012</div><div class="comment-text">Brightmoor Web Studio provides you the Search Engine Optimization making your website search engine friendly.</div><div class="comment-more">READ MORE &rsaquo;</div></div>
  <div class="comment"><div class="comment-date">20.March.2012</div><div class="comment-text">E-Commerce is a major progress in technology that has changed the way</div><div class="comment-more">READ MORE &rsaquo;</div></div>
  <div class="comment"><div class="comment-date">20.March.2012</div><div class="comment-text">E-Commerce is a major progress in technology that has changed the way</div><div class="comment-more">READ MORE &rsaquo;</div></div>
</aside>

<aside class="abs saving">
  <div class="abs saving-img" role="img" aria-label="Hand dropping a coin into a glass piggy bank full of coins"></div>
  <div class="abs saving-learn">Learn</div>
  <div class="abs saving-copy">the saving culture to<br>Investment Opportunities</div>
</aside>

<footer class="abs footer">
  <div class="abs footer-nav">Home<span>|</span>About Us<span>|</span>Membership<span>|</span>Member Projects<span>|</span>Membership Levels<span>|</span>Links<span>|</span>Contact Us</div>
  <div class="abs footer-copy">Kindred Road Trust Order. © 2012. All rights reserved.</div>
  <div class="abs social"><i></i><i></i><i></i></div>
</footer>

</body>
</html>
```